" A empresa em questao será uma clínica médica e de fisioterapia especializada em tratamento de coluna. Tanto os médicos quanto os tratamentos fisioterápicos (fisioterapia, osteopatia, RPG) serao direcionados para o público que busca tratamento e soluçoes para dores nas costas em geral. "

```html
<!DOCTYPE html>
<html lang="pt-BR">
<head>
<meta charset="UTF-8">
<title>Clínica Eixo Vital — Papel timbrado</title>
<link rel="stylesheet" href="https://fonts.googleapis.com/css2?family=Cormorant+Garamond:wght@500&family=Open+Sans:wght@400&display=swap">
<style>
  :root {
    --backdrop: #ecebe8;
    --paper: #ffffff;
    --band: #000000;
    --band-text: #ffffff;
    --mark-faint: #e9e9e9;
    --footer-bar: #a7a7a7;
    --footer-text: #ffffff;
  }
  * { margin: 0; padding: 0; box-sizing: border-box; }
  html, body {
    width: 1200px;
    height: 1200px;
    overflow: hidden;
    background: var(--backdrop);
  }
  .letterhead {
    position: absolute;
    left: 240px;
    top: 105px;
    width: 720px;
    height: 990px;
    background: var(--paper);
    box-shadow: 0 6px 18px rgba(0,0,0,0.18);
  }
  .header-band {
    position: absolute;
    left: 0;
    top: 35px;
    width: 100%;
    height: 95px;
    background: var(--band);
    display: flex;
    align-items: center;
    justify-content: center;
  }
  .brand {
    display: flex;
    align-items: center;
    gap: 14px;
    color: var(--band-text);
  }
  .brand-dot {
    width: 42px;
    height: 42px;
    border: 2px solid var(--band-text);
    border-radius: 50%;
  }
  .brand-name {
    font-family: "Cormorant Garamond", serif;
    font-weight: 500;
    font-size: 22px;
    line-height: 1.05;
    letter-spacing: 1px;
    text-transform: uppercase;
  }
  .watermark {
    position: absolute;
    left: 100px;
    top: 370px;
    width: 520px;
    height: 520px;
  }
  .footer-bar {
    position: absolute;
    left: 87px;
    top: 952px;
    width: 563px;
    height: 30px;
    background: var(--footer-bar);
    color: var(--footer-text);
    font-family: "Open Sans", sans-serif;
    font-size: 12px;
    display: flex;
    align-items: center;
    justify-content: center;
    white-space: nowrap;
  }
</style>
</head>
<body>
  <main class="letterhead">
    <header class="header-band">
      <div class="brand">
        <span class="brand-dot"></span>
        <span class="brand-name">Clínica<br>Eixo Vital</span>
      </div>
    </header>

    <svg class="watermark" viewBox="0 0 520 520" aria-hidden="true">
      <circle cx="260" cy="260" r="238" fill="none" stroke="var(--mark-faint)" stroke-width="42"/>
    </svg>

    <footer class="footer-bar">Rua Sem Nome,00 Bairro Sem Nome Cidade Sem Nome &nbsp;- Cep 00.000-000</footer>
  </main>
</body>
</html>
```